web page layout, style , color, font & flow design

We are developing a single page application. The SPA (single page application) will display natural gas pipeline flow data once the customer logs on. The customer has a choice of the region, the pipeline, the zone on the pipeline, whether the point is a delivery point or receipt point and the state the pipeline flows through.
we have jumpstarted the project and are attaching a pdf of the same.

we are using mockingbird for the wireframe. any designer is free to use this tool to make changes.

A mockingbird wireframe link is added below. you are free to use it and to make changes. please save the changed wireframe in a different name

we are looking for inputs on layout, style , color, font & flow.

A logo jpg file has also been attached.

Target Market(s)

this single web page is going to be used by natural gas traders and schedulers day in and day out. the application is more of business to business corporate application.

Industry/Entity Type

Delivery

Requirements
Must have
• layout ,flow, size, color, font , ease of use.

```html
<!DOCTYPE html>
<html lang="en">
<head>
<meta charset="utf-8">
<title>Search Preferences – Layout Options</title>
<link href="https://fonts.googleapis.com/css2?family=Arimo:wght@400;700&display=swap" rel="stylesheet">
<style>
  :root{
    --page-bg:#ffffff;
    --caption:#1b1b1b;
    --header-top:#1570d6;
    --header-bottom:#0055bb;
    --header-text:#ffffff;
    --row-top:#ffffff;
    --row-bottom:#f2f2f2;
    --row-line:#e1e1e1;
    --row-title:#1467c8;
    --panel-line:#d9d9d9;
    --toggle:#a9a9a9;
    --label:#4a4a4a;
    --field-line:#d5d5d5;
    --field-text:#666666;
    --arrow:#0d5bc0;
    --well:#f3f2f2;
    --go-top:#7fdc48;
    --go-bottom:#62c930;
    --go-text:#ffffff;
  }
  *{box-sizing:border-box;margin:0;padding:0}
  html,body{width:1200px;height:724px;overflow:hidden;background:var(--page-bg)}
  body{font-family:"Arimo",Arial,sans-serif}
  .board{position:relative;width:1240px;height:748px;transform:scale(0.9677);transform-origin:0 0}
  .caption{position:absolute;font-size:12px;color:var(--caption);letter-spacing:.1px;text-transform:uppercase}
  .panel{position:absolute;width:339px;border:1px solid var(--panel-line);border-top:none;background:#fff}
  .panel-header{position:relative;height:43px;background:linear-gradient(var(--header-top),var(--header-bottom));color:var(--header-text);font-size:14.5px;border-radius:2px 2px 0 0}
  .panel-header .valve{position:absolute;left:17px;top:14px}
  .panel-header .title{position:absolute;left:50px;top:14px}
  .panel-header .chevron{position:absolute;right:20px;top:17px}
  .section-head{position:relative;height:54px;background:linear-gradient(var(--row-top),var(--row-bottom));border-bottom:1px solid var(--row-line)}
  .section-head .name{position:absolute;left:16px;top:21px;font-size:13px;font-weight:700;color:var(--row-title)}
  .section-head .toggle{position:absolute;right:21px;top:20px}
  .section-body{position:relative;border-bottom:1px solid var(--row-line)}
  .label{position:absolute;font-size:12.5px;color:var(--label);line-height:16px}
  .select{position:absolute;height:31px;width:218px;border:1px solid var(--field-line);background:#fff;font-size:12.5px;color:var(--field-text)}
  .select .value{position:absolute;left:10px;top:8px}
  .select .arrow{position:absolute;right:0;top:0;width:31px;height:29px;border-left:1px solid var(--field-line);display:flex;align-items:center;justify-content:center}
  .check{position:absolute;font-size:12.5px;color:var(--label);display:flex;align-items:center;gap:8px}
  .check .box{width:19px;height:19px;border:1px solid var(--field-line);background:#fff;box-shadow:inset 1px 1px 2px rgba(0,0,0,.08)}
  .search-btn{position:absolute;width:191px;height:25px;border:none;border-radius:2px;background:linear-gradient(var(--go-top),var(--go-bottom));color:var(--go-text);font:700 13px "Arimo",Arial,sans-serif;text-align:center;line-height:25px}
  .well{position:absolute;left:8px;top:51px;width:321px;height:272px;background:var(--well)}
</style>
</head>
<body>
<div class="board">

  <p class="caption" style="left:48px;top:19px">1. Search Preferences “Not Expanded”</p>
  <p class="caption" style="left:426px;top:14px">1.a Search Preferences “Expanded”</p>
  <p class="caption" style="left:841px;top:10px">2. Simpe Search Preferences</p>

  <!-- Collapsed -->
  <section class="panel" style="left:40px;top:51px;height:325px">
    <header class="panel-header">
      <svg class="valve" width="20" height="14" viewBox="0 0 20 14"><rect x="8" y="0" width="4" height="5" fill="#fff"/><rect x="5" y="0" width="10" height="2" fill="#fff"/><rect x="0" y="5" width="20" height="6" rx="1" fill="#fff"/><rect x="0" y="4" width="2" height="8" fill="#fff"/><rect x="18" y="4" width="2" height="8" fill="#fff"/></svg>
      <span class="title">Search Preferences</span>
      <svg class="chevron" width="18" height="10" viewBox="0 0 18 10"><path d="M1 1l8 8 8-8" fill="none" stroke="#fff" stroke-width="1.5"/></svg>
    </header>
    <div class="section-head"><span class="name">Pipeline Region</span><svg class="toggle" width="15" height="15" viewBox="0 0 15 15"><circle cx="7.5" cy="7.5" r="7.5" fill="var(--toggle)"/><path d="M3.5 7.5h8M7.5 3.5v8" stroke="#fff" stroke-width="2"/></svg></div>
    <div class="section-head"><span class="name">Pipeline Zone</span><svg class="toggle" width="15" height="15" viewBox="0 0 15 15"><circle cx="7.5" cy="7.5" r="7.5" fill="var(--toggle)"/><path d="M3.5 7.5h8M7.5 3.5v8" stroke="#fff" stroke-width="2"/></svg></div>
    <div class="section-head"><span class="name">Pipeline Type</span><svg class="toggle" width="15" height="15" viewBox="0 0 15 15"><circle cx="7.5" cy="7.5" r="7.5" fill="var(--toggle)"/><path d="M3.5 7.5h8M7.5 3.5v8" stroke="#fff" stroke-width="2"/></svg></div>
    <div class="section-head"><span class="name">State of the Pipeline</span><svg class="toggle" width="15" height="15" viewBox="0 0 15 15"><circle cx="7.5" cy="7.5" r="7.5" fill="var(--toggle)"/><path d="M3.5 7.5h8M7.5 3.5v8" stroke="#fff" stroke-width="2"/></svg></div>
    <div class="search-btn" style="left:75px;top:280px">Search</div>
  </section>

  <!-- Expanded -->
  <section class="panel" style="left:419px;top:51px;height:676px">
    <header class="panel-header">
      <svg class="valve" width="20" height="14" viewBox="0 0 20 14"><rect x="8" y="0" width="4" height="5" fill="#fff"/><rect x="5" y="0" width="10" height="2" fill="#fff"/><rect x="0" y="5" width="20" height="6" rx="1" fill="#fff"/><rect x="0" y="4" width="2" height="8" fill="#fff"/><rect x="18" y="4" width="2" height="8" fill="#fff"/></svg>
      <span class="title">Search Preferences</span>
      <svg class="chevron" width="18" height="10" viewBox="0 0 18 10"><path d="M1 1l8 8 8-8" fill="none" stroke="#fff" stroke-width="1.5"/></svg>
    </header>
    <div class="section-head"><span class="name">Pipeline Region</span><svg class="toggle" width="15" height="15" viewBox="0 0 15 15"><circle cx="7.5" cy="7.5" r="7.5" fill="var(--toggle)"/><path d="M3.5 7.5h8" stroke="#fff" stroke-width="2"/></svg></div>
    <div class="section-body" style="height:94px">
      <span class="label" style="left:16px;top:38px">Region:</span>
      <div class="select" style="left:91px;top:29px"><span class="value">Choose&nbsp; Region</span><span class="arrow"><svg width="12" height="8" viewBox="0 0 12 8"><path d="M0 0h12L6 8z" fill="var(--arrow)"/></svg></span></div>
    </div>
    <div class="section-head"><span class="name">Pipeline Zone</span><svg class="toggle" width="15" height="15" viewBox="0 0 15 15"><circle cx="7.5" cy="7.5" r="7.5" fill="var(--toggle)"/><path d="M3.5 7.5h8" stroke="#fff" stroke-width="2"/></svg></div>
    <div class="section-body" style="height:95px">
      <span class="label" style="left:16px;top:39px">Zone:</span>
      <div class="select" style="left:91px;top:29px"><span class="value">Choose&nbsp; Zone</span><span class="arrow"><svg width="12" height="8" viewBox="0 0 12 8"><path d="M0 0h12L6 8z" fill="var(--arrow)"/></svg></span></div>
    </div>
    <div class="section-head"><span class="name">Pipeline Type</span><svg class="toggle" width="15" height="15" viewBox="0 0 15 15"><circle cx="7.5" cy="7.5" r="7.5" fill="var(--toggle)"/><path d="M3.5 7.5h8" stroke="#fff" stroke-width="2"/></svg></div>
    <div class="section-body" style="height:81px">
      <span class="check" style="left:24px;top:31px"><span class="box"></span>Delivery Point</span>
      <span class="check" style="left:164px;top:31px"><span class="box"></span>Receipt Point</span>
    </div>
    <div class="section-head"><span class="name">State of the Pipeline</span><svg class="toggle" width="15" height="15" viewBox="0 0 15 15"><circle cx="7.5" cy="7.5" r="7.5" fill="var(--toggle)"/><path d="M3.5 7.5h8" stroke="#fff" stroke-width="2"/></svg></div>
    <span class="label" style="left:21px;top:556px">State of the<br>Pipeline:</span>
    <div class="select" style="left:97px;top:557px"><span class="value">Available</span><span class="arrow"><svg width="12" height="8" viewBox="0 0 12 8"><path d="M0 0h12L6 8z" fill="var(--arrow)"/></svg></span></div>
    <div class="search-btn" style="left:64px;top:623px">Search</div>
  </section>

  <!-- Simple -->
  <section class="panel" style="left:831px;top:49px;height:333px">
    <header class="panel-header">
      <svg class="valve" width="20" height="14" viewBox="0 0 20 14"><rect x="8" y="0" width="4" height="5" fill="#fff"/><rect x="5" y="0" width="10" height="2" fill="#fff"/><rect x="0" y="5" width="20" height="6" rx="1" fill="#fff"/><rect x="0" y="4" width="2" height="8" fill="#fff"/><rect x="18" y="4" width="2" height="8" fill="#fff"/></svg>
      <span class="title">Search Preferences</span>
      <svg class="chevron" width="18" height="10" viewBox="0 0 18 10"><path d="M1 1l8 8 8-8" fill="none" stroke="#fff" stroke-width="1.5"/></svg>
    </header>
    <div class="well">
      <span class="label" style="left:11px;top:22px">Region:</span>
      <div class="select" style="left:87px;top:12px"><span class="value">Choose&nbsp; Region</span><span class="arrow"><svg width="12" height="8" viewBox="0 0 12 8"><path d="M0 0h12L6 8z" fill="var(--arrow)"/></svg></span></div>
      <span class="label" style="left:13px;top:70px">Zone:</span>
      <div class="select" style="left:89px;top:60px"><span class="value">Choose&nbsp; Zone</span><span class="arrow"><svg width="12" height="8" viewBox="0 0 12 8"><path d="M0 0h12L6 8z" fill="var(--arrow)"/></svg></span></div>
      <span class="check" style="left:13px;top:118px"><span class="box"></span>Delivery Point</span>
      <span class="check" style="left:153px;top:118px"><span class="box"></span>Receipt Point</span>
      <span class="label" style="left:13px;top:164px">State of the<br>Pipeline:</span>
      <div class="select" style="left:89px;top:164px"><span class="value">Available</span><span class="arrow"><svg width="12" height="8" viewBox="0 0 12 8"><path d="M0 0h12L6 8z" fill="var(--arrow)"/></svg></span></div>
      <div class="search-btn" style="left:64px;top:224px">Search</div>
    </div>
  </section>

</div>
</body>
</html>
```